Briskly Verdant Vessel Plots

We need a socialnook page designed that matches the logo on our business card (See separate brief on Pixel Forum). We are a small business that design compact succulent gardens using our imagination to pair the natural qualities of the plants with their containers. Wherever possible we carefully select upcycled, quirky, vintage and recycled materials for our containers so that each piece is unique. Succulents require very little maintenance and in Spring and Summer will delight and suprise you with their unexpected and sometimes quite spectacular display of flowers. We also offer a small range of delightful individually handcrafted garden art windchimes and mobiles also made from carefully selected vintage items.
Contact Information : Message Me @ SN or email Moira via Briskly.Verdant@fernpost.example to arrange pick up and address details in Wendmoor Brisbane.

(CAN YOU PLEASE DELETE ANY PICS WHICH ARE BADLY OUT OF FOCUS - I HAVE A LOT OF TROUBLE WITH MY DSLR CAMERA AS MY EYES ARE GETTING BAD)

I would like the Echinevera Lilac Rose as our Logo if possible but the photo came from imagevault and should be attributed somewhere to "lanternfox."

thanks Moira

This project has been bundled with a Business Card Design Project: http://jobs.pixelforum.example/job.aspx?id=517064

I encourage you to submit to both projects and keep designs consistent.

Target Market(s)

The target market is adults in South East Queensland aged 18 -75 looking for unusual and personalised gifts particularly for people who enjoy gardening or live in an apartment wth limited opportunity for gardening and those who appreciate vintage, quirky and upcycled things.

Industry/Entity Type

Small Business

Font styles to use
Script

Colors

Designer to choose colors to be used in the design.

Requirements
Must have

• I would like the Echinevera Lilac Rose as our Logo if possible but the photo came from imagevault and should be attributed somewhere to "lanternfox." This photo is in the bottom right hand corner.

The SN page must complement and be consistent with the "branding" on the business cards project.
Nice to have
• I quite like the script type of font but not too curly and feminine as this product has to appeal to men and women alike. So something a bit sophisticated but not "girly"

I quite like the second pic in the second row of the faces and curly tales and the first two shots in the bottom row should go on the SN page somewhere as a collection of current stock (though it is constantly growing - pardon the pun)
Should not have
• (CAN YOU PLEASE DELETE ANY PICS I have uploaded WHICH ARE BADLY OUT OF FOCUS - I HAVE A LOT OF TROUBLE WITH MY DSLR CAMERA AS MY EYES ARE GETTING BAD)

There are some minatures there which have been planted in corks and mounted on boards with stencil decorations - these obviously need to be turned around 90 degrees.

```html
<!DOCTYPE html>
<html lang="en">
<head>
<meta charset="utf-8">
<title>Briskly Verdant – socialnook page</title>
<link rel="stylesheet" href="https://fonts.googleapis.com/css2?family=Arimo:wght@400;700&family=Tinos:wght@400;700&display=swap">
<style>
  :root {
    --bar-blue: #3f5c9a;
    --bar-edge: #2c4375;
    --link-blue: #3b5998;
    --page-bg: #e9eaed;
    --panel: #ffffff;
    --panel-line: #d3d6db;
    --text: #1d2129;
    --muted: #90949c;
    --soft: #4b4f56;
    --button-bg: #f6f7f9;
    --button-line: #ced0d4;
    --nav-line: #c4cde0;
    --nav-active: #5874a8;
    --cover-pink: #b0286a;
    --cover-deep: #8c1650;
    --cover-gold: #b08a3a;
    --cover-leaf: #5c7a3e;
    --white: #ffffff;
  }
  * { box-sizing: border-box; margin: 0; padding: 0; }
  html, body { width: 1200px; height: 690px; overflow: hidden; }
  body {
    position: relative;
    background: var(--page-bg);
    font-family: "Arimo", Helvetica, Arial, sans-serif;
    color: var(--text);
  }

  /* top bar */
  .top-bar {
    position: absolute; left: 0; top: 0; width: 1200px; height: 45px;
    background: var(--bar-blue); border-bottom: 1px solid var(--bar-edge);
  }
  .brand { position: absolute; left: 58px; top: 9px; display: flex; align-items: center; gap: 6px; }
  .brand-mark { width: 25px; height: 25px; background: var(--white); }
  .brand-name { display: none; }
  .search {
    position: absolute; left: 92px; top: 8px; width: 648px; height: 26px;
    background: var(--white); border: 1px solid var(--bar-edge); border-radius: 2px;
    font-size: 15px; line-height: 24px; padding-left: 9px; color: var(--text);
  }
  .search svg { position: absolute; right: 8px; top: 4px; }
  .home-link {
    position: absolute; left: 1062px; top: 0; height: 45px; padding-left: 13px;
    border-left: 1px solid var(--bar-edge);
    color: var(--white); font-size: 12px; font-weight: 700; line-height: 48px;
  }
  .home-caret { position: absolute; left: 1128px; top: 21px; }

  /* cover */
  .cover {
    position: absolute; left: 50px; top: 45px; width: 951px; height: 350px;
    background: linear-gradient(100deg, var(--cover-pink) 0%, var(--cover-deep) 35%, var(--cover-pink) 48%, var(--cover-gold) 62%, var(--cover-leaf) 75%, var(--cover-gold) 90%, var(--cover-pink) 100%);
  }
  .cover-title {
    position: absolute; left: 30px; top: 8px;
    font-family: "Tinos", "Times New Roman", serif; font-weight: 400;
    font-size: 68px; line-height: 63px;
    color: var(--white);
  }
  .page-name {
    position: absolute; left: 290px; top: 333px;
    font-size: 27px; font-weight: 700; color: var(--white);
  }
  .page-category {
    position: absolute; left: 290px; top: 369px;
    font-size: 16px; color: var(--white);
  }

  /* profile picture */
  .profile-frame {
    position: absolute; z-index: 2; left: 76px; top: 280px; width: 190px; height: 188px;
    background: var(--white); border: 1px solid var(--panel-line); padding: 4px;
  }
  .profile-photo {
    position: relative; width: 100%; height: 100%;
    background: radial-gradient(circle at 55% 42%, var(--cover-leaf) 0%, var(--cover-gold) 30%, var(--cover-pink) 60%, var(--cover-deep) 100%);
  }
  .profile-initials {
    position: absolute; left: 0; right: 0; bottom: 8px; text-align: center;
    font-family: "Tinos", "Times New Roman", serif; font-size: 40px; color: var(--white);
  }

  /* tab strip */
  .tab-strip {
    position: absolute; z-index: 1; left: 50px; top: 395px; width: 951px; height: 86px;
    background: var(--panel); border-bottom: 1px solid var(--panel-line);
  }
  .tabs { position: absolute; left: 226px; top: 20px; width: 414px; height: 36px; border-bottom: 3px solid var(--panel-line); display: flex; }
  .tab { font-size: 15.5px; color: var(--soft); padding: 0 22px; line-height: 28px; border-right: 1px solid var(--panel-line); height: 28px; }
  .tab:last-child { border-right: none; }
  .tab.active { font-weight: 700; color: var(--text); padding-left: 10px; position: relative; }
  .tab.active::after { content: ""; position: absolute; left: 2px; right: 2px; top: 33px; height: 3px; background: var(--nav-active); }
  .button {
    position: absolute; top: 20px; height: 28px;
    background: var(--button-bg); border: 1px solid var(--button-line); border-radius: 2px;
    font-size: 14.5px; font-weight: 700; color: var(--soft); line-height: 26px;
  }
  .like-button { left: 710px; width: 70px; padding-left: 26px; }
  .like-button svg { position: absolute; left: 8px; top: 6px; }
  .message-button { left: 792px; width: 131px; padding-left: 9px; }
  .message-button .gear { position: absolute; left: 83px; top: 0; width: 47px; height: 26px; border-left: 1px solid var(--button-line); }
  .message-button svg { position: absolute; left: 8px; top: 7px; }

  /* right rail */
  .create-page {
    position: absolute; left: 1016px; top: 59px; width: 91px; height: 24px;
    background: var(--link-blue); border: 1px solid var(--bar-edge); border-radius: 2px;
    color: var(--white); font-size: 12.5px; font-weight: 700; text-align: center; line-height: 22px;
  }
  .rail-divider { position: absolute; left: 1016px; top: 98px; width: 184px; height: 1px; background: var(--panel-line); }
  .year-nav { position: absolute; left: 1016px; top: 108px; list-style: none; }
  .year-nav li {
    height: 25.5px; padding-left: 12px; border-left: 4px solid var(--nav-line);
    font-size: 12.5px; line-height: 25px; color: var(--muted);
  }
  .year-nav li.current { border-left-color: var(--nav-active); color: var(--link-blue); font-weight: 700; }

  /* left column */
  .card { position: absolute; background: var(--panel); border: 1px solid var(--panel-line); border-radius: 3px; }
  .card-head {
    height: 41px; border-bottom: 1px solid var(--panel-line);
    font-size: 12px; font-weight: 700; color: var(--soft); line-height: 41px; padding-left: 13px; position: relative;
  }
  .card-head svg { position: absolute; right: 14px; top: 14px; }
  .people-card { left: 51px; top: 484px; width: 366px; height: 133px; }
  .like-count { height: 51px; border-bottom: 1px solid var(--panel-line); text-align: center; font-size: 15px; color: var(--muted); line-height: 51px; }
  .like-count b { color: var(--text); font-size: 17px; }
  .invite { font-size: 13.5px; color: var(--link-blue); padding-left: 13px; line-height: 40px; }
  .about-card { left: 51px; top: 632px; width: 366px; height: 70px; }

  /* post */
  .post-card { left: 430px; top: 484px; width: 571px; height: 220px; }
  .post-avatar {
    position: absolute; left: 7px; top: 12px; width: 52px; height: 46px;
    background: radial-gradient(circle at 50% 45%, var(--cover-leaf) 0%, var(--cover-gold) 35%, var(--cover-pink) 70%);
  }
  .post-author { position: absolute; left: 68px; top: 18px; font-size: 13.5px; font-weight: 700; color: var(--link-blue); }
  .post-date { position: absolute; left: 68px; top: 37px; font-size: 12.5px; color: var(--muted); }
  .post-date svg { vertical-align: -1px; margin-left: 3px; }
  .post-caret { position: absolute; right: 13px; top: 16px; }
  .post-body { position: absolute; left: 14px; top: 79px; width: 545px; font-size: 15.5px; line-height: 22.4px; color: var(--text); }
  .post-body span { display: block; white-space: nowrap; }
  .post-body .see-more { display: inline; color: var(--link-blue); }
</style>
</head>
<body>

<header class="top-bar">
  <div class="brand"><div class="brand-mark"></div><span class="brand-name">socialnook</span></div>
  <div class="search">Briskly Verdant
    <svg width="17" height="17" viewBox="0 0 17 17" aria-hidden="true"><circle cx="7" cy="7" r="5.5" fill="none" stroke="#4b4f56" stroke-width="2"/><line x1="11" y1="11" x2="15.5" y2="15.5" stroke="#4b4f56" stroke-width="2.2"/></svg>
  </div>
  <div class="home-link">Home</div>
  <svg class="home-caret" width="9" height="5" viewBox="0 0 9 5" aria-hidden="true"><polygon points="0,0 9,0 4.5,5" fill="#ffffff"/></svg>
</header>

<section class="cover" role="img" aria-label="Cover photo: star-shaped gold dish planted with succulents and river pebbles on a magenta cloth">
  <h1 class="cover-title">Briskly<br>Verdant</h1>
</section>
<div class="page-name">Briskly Verdant</div>
<div class="page-category">Local Business</div>

<div class="profile-frame">
  <div class="profile-photo" role="img" aria-label="Profile photo: star dish of succulents on magenta">
    <div class="profile-initials">BV</div>
  </div>
</div>

<nav class="tab-strip">
  <div class="tabs">
    <div class="tab active">Timeline</div>
    <div class="tab">About</div>
    <div class="tab">Photos</div>
    <div class="tab">Likes</div>
    <div class="tab">Videos</div>
  </div>
  <div class="button like-button">
    <svg width="14" height="14" viewBox="0 0 14 14" aria-hidden="true"><rect x="1" y="6" width="3" height="7" fill="none" stroke="#4b4f56" stroke-width="1.3"/><path d="M5 6 L8 1 Q9.5 1 9 4 L8.6 5.5 H12.5 Q13.4 6 12.8 7.5 L11.6 12.3 Q11.2 13 10.4 13 H5 Z" fill="none" stroke="#4b4f56" stroke-width="1.3"/></svg>
    Like</div>
  <div class="button message-button">Message
    <div class="gear">
      <svg width="30" height="12" viewBox="0 0 30 12" aria-hidden="true"><circle cx="6" cy="6" r="3.5" fill="none" stroke="#4b4f56" stroke-width="2.4" stroke-dasharray="2 1.4"/><polygon points="21,4 29,4 25,8.5" fill="#5874a8"/></svg>
    </div>
  </div>
</nav>

<aside>
  <div class="create-page">Create Page</div>
  <div class="rail-divider"></div>
  <ul class="year-nav">
    <li class="current">Now</li>
    <li>October</li>
    <li>2012</li>
    <li>2011</li>
    <li>Founded</li>
  </ul>
</aside>

<section class="card people-card">
  <div class="card-head">PEOPLE
    <svg width="8" height="13" viewBox="0 0 8 13" aria-hidden="true"><polyline points="1,1 6.5,6.5 1,12" fill="none" stroke="#4b4f56" stroke-width="2"/></svg>
  </div>
  <div class="like-count"><b>14</b> likes</div>
  <div class="invite">Invite your friends to like this Page</div>
</section>

<section class="card about-card">
  <div class="card-head">ABOUT
    <svg width="8" height="13" viewBox="0 0 8 13" aria-hidden="true"><polyline points="1,1 6.5,6.5 1,12" fill="none" stroke="#4b4f56" stroke-width="2"/></svg>
  </div>
</section>

<article class="card post-card">
  <div class="post-avatar" role="img" aria-label="Page avatar: star dish of succulents"></div>
  <div class="post-author">Briskly Verdant</div>
  <div class="post-date">November 23
    <svg width="11" height="11" viewBox="0 0 11 11" aria-hidden="true"><circle cx="5.5" cy="5.5" r="4.8" fill="#90949c"/><circle cx="5.5" cy="5.5" r="2" fill="#ffffff"/></svg>
  </div>
  <svg class="post-caret" width="12" height="7" viewBox="0 0 12 7" aria-hidden="true"><polyline points="1,1 6,6 11,1" fill="none" stroke="#c4c7cc" stroke-width="1.5"/></svg>
  <p class="post-body">
    <span>Today was the first day of trading at the Harrowdale Markets - well the 4.30am</span>
    <span>start on a Sunday morning was definitely a shock to the system but we were</span>
    <span>soon upacking our products and setting up our stall. What an extraordinary</span>
    <span>experience to watch so many early birds rushing about looking to catch their</span>
    <span>particular worms. While I couldnt claim that we had the most successful</span>
    <span>trading day- we did rec... <span class="see-more">See More</span></span>
  </p>
</article>

</body>
</html>
```